"Silver Rivers Rollin'" cd cover/logo design

I am a vocalist, arranger and composer/producer currently recording cd. I need an artist that can capture the following:
Sillouette of man sitting sideways (full body) on stoop with a brickface backround. The man is mostly in black with a "campesino" (can describe) straw hat on in lavendar color. Man also has parrot on his arm with one wing down and the other upright. Parrott is facing man. Actual colors of parrot will be supplied by photo. Man's skin and skin color of face and hands revealed.
Brickface back drop will clearly list in graffitti type lettering title of album ("Silver Rivers Rollin") in white along with artist name (Oraanu V'Marsk).
Final product should be "urban classy" design to be utilized as artist logo and cd cover.
Target Market(s)
World music fans of all ages
Actual works combine Afro Latin , Uptempo Blues/Jazz, House dance
Industry/Entity Type
Product
Font styles to use
Other font styles liked:
- legible graffitti
Look and feel
Each slider illustrates characteristics of the customer's brand and the style your logo design should communicate.

```html
<!DOCTYPE html>
<html lang="en">
<head>
<meta charset="utf-8">
<title>Silver Rivers Rollin – Oraanu V'Marsk</title>
<link rel="stylesheet" href="https://fonts.googleapis.com/css2?family=Caveat+Brush&family=Gochi+Hand&display=swap">
<style>
  :root {
    --brick-light: #c0654a;
    --brick-mid: #a9523b;
    --brick-dark: #8d4433;
    --mortar: #b9a79c;
    --lettering: #eefde6;
    --figure-dark: #3a272c;
    --hat-lavender: #c98bbd;
    --skin: #d9773a;
  }
  * { margin: 0; padding: 0; box-sizing: border-box; }
  html, body {
    width: 1200px;
    height: 1200px;
    overflow: hidden;
    background: var(--brick-mid);
  }
  .cover {
    position: relative;
    width: 1200px;
    height: 1200px;
    overflow: hidden;
  }
  .brick-wall {
    position: absolute;
    inset: 0;
    background: linear-gradient(160deg, var(--brick-light) 0%, var(--brick-mid) 55%, var(--brick-dark) 100%);
  }
  .figure-with-parrot {
    position: absolute;
    left: 690px;
    top: 470px;
    width: 510px;
    height: 730px;
    background: linear-gradient(180deg, var(--hat-lavender) 0%, var(--skin) 38%, var(--figure-dark) 62%, var(--figure-dark) 100%);
    border-radius: 180px 40px 0 60px;
  }
  .label-line {
    position: absolute;
    left: 82px;
    top: 14px;
    font-family: "Gochi Hand", cursive;
    font-size: 62px;
    line-height: 1;
    color: var(--lettering);
    letter-spacing: 1px;
  }
  .album-title {
    position: absolute;
    left: 80px;
    top: 40px;
    font-family: "Caveat Brush", cursive;
    font-size: 300px;
    line-height: 250px;
    color: var(--lettering);
    text-transform: lowercase;
  }
  .album-title span { display: block; }
  .artist-name {
    position: absolute;
    left: 78px;
    top: 880px;
    font-family: "Caveat Brush", cursive;
    font-size: 165px;
    line-height: 125px;
    color: var(--lettering);
    text-transform: lowercase;
  }
  .artist-name span { display: block; }
</style>
</head>
<body>
  <main class="cover">
    <div class="brick-wall" role="img" aria-label="Red brick wall backdrop"></div>
    <div class="figure-with-parrot" role="img" aria-label="Silhouette of a man sitting on a stoop in black clothes and a lavender straw hat, with a green parrot perched on his arm"></div>

    <p class="label-line">LunaReed Music presents</p>

    <h1 class="album-title">
      <span>silver</span>
      <span>rivers</span>
      <span>rollin</span>
    </h1>

    <h2 class="artist-name">
      <span>oraanu</span>
      <span>v'marsk</span>
    </h2>
  </main>
</body>
</html>
```